Harbinger Crude Advisors needs a logo design and business card layout.

HCA is a consulting firm in oil and gas, specializing in upstream engineering and field work. We provide engineering solutions for the complete wellbore cycle from casing design to flowback. This includes completion and production design. On-site job supervision and project engineering for conventional and unconventional reservoirs. Asset analysis by reviewing operational conditions of asset packages to determine value of potential acquisitions or divesture.

```html
<!DOCTYPE html>
<html lang="en">
<head>
<meta charset="utf-8">
<title>Harbinger Crude Advisors – Business Card</title>
<link href="https://fonts.googleapis.com/css2?family=Lato:wght@400;700&display=swap" rel="stylesheet">
<style>
  :root {
    --backdrop: #262627;
    --card: #1b1b1c;
    --ink: #dcdcdc;
    --ink-muted: #a9a9aa;
    --rule: #5a5a5b;
  }
  * { margin: 0; padding: 0; box-sizing: border-box; }
  html, body {
    width: 1200px; height: 900px; overflow: hidden;
    background: var(--backdrop);
    font-family: "Lato", sans-serif;
  }
  .canvas {
    width: 1200px; height: 900px;
    display: flex; flex-direction: column;
    align-items: center; justify-content: center; gap: 28px;
  }
  .card {
    width: 700px; height: 400px;
    background: var(--card);
    position: relative;
  }
  .card-front {
    display: flex; align-items: center; justify-content: center;
  }
  .wordmark { text-align: left; color: var(--ink); font-weight: 700; }
  .wordmark-initials {
    font-size: 120px; line-height: 1; letter-spacing: 4px;
  }
  .wordmark-name {
    font-size: 15px; letter-spacing: 2.5px; text-transform: uppercase;
    margin-top: 6px;
  }
  .card-back { display: flex; align-items: center; }
  .card-back .brand-block {
    width: 360px; padding-left: 48px;
  }
  .card-back .wordmark-initials { font-size: 96px; }
  .card-back .wordmark-name { font-size: 12px; letter-spacing: 2px; }
  .divider {
    width: 1px; height: 210px; background: var(--rule);
  }
  .contact-block { padding-left: 30px; color: var(--ink); }
  .person-name {
    font-size: 27px; font-weight: 400; letter-spacing: 1.5px;
    text-transform: uppercase;
  }
  .person-title { font-size: 15px; color: var(--ink-muted); margin-bottom: 20px; }
  .address { font-size: 15px; line-height: 1.45; margin-bottom: 6px; }
  .contact-line {
    display: flex; align-items: center; gap: 10px;
    font-size: 16px; line-height: 1.55;
  }
  .contact-line svg { width: 12px; height: 12px; flex: none; }
  .contact-line .icon-spacer { width: 12px; flex: none; }
</style>
</head>
<body>
<main class="canvas">
  <section class="card card-front">
    <div class="wordmark">
      <div class="wordmark-initials">HCA</div>
      <div class="wordmark-name">Harbinger Crude Advisors</div>
    </div>
  </section>

  <section class="card card-back">
    <div class="brand-block">
      <div class="wordmark">
        <div class="wordmark-initials">HCA</div>
        <div class="wordmark-name">Harbinger Crude Advisors</div>
      </div>
    </div>
    <div class="divider"></div>
    <div class="contact-block">
      <h1 class="person-name">Darren Holloway</h1>
      <p class="person-title">Director</p>
      <p class="address">4417 W. Mesa Ridge Dr.<br>#212 Tempe, AZ 85281</p>
      <p class="contact-line">
        <svg viewBox="0 0 12 12" fill="var(--ink-muted)"><path d="M2.5 1l2 2.2-1.2 1.3c.7 1.5 1.8 2.6 3.2 3.2l1.3-1.2L10 8.5 8.8 10.8C4.6 10.4 1.6 7.4 1.2 3.2z"/></svg>
        (480) 555-0147
      </p>
      <p class="contact-line">
        <svg viewBox="0 0 12 12" fill="none" stroke="var(--ink-muted)" stroke-width="1.2"><rect x="1" y="2.5" width="10" height="7"/><path d="M1 2.5l5 4 5-4"/></svg>
        info@harbingercrude.com
      </p>
      <p class="contact-line">
        <svg viewBox="0 0 12 12" fill="none" stroke="var(--ink-muted)" stroke-width="1.1"><circle cx="6" cy="6" r="5"/><ellipse cx="6" cy="6" rx="2.2" ry="5"/><path d="M1 6h10"/></svg>
        www.harbingercrude.com
      </p>
    </div>
  </section>
</main>
</body>
</html>
```